Finance web application design

We need a design for a new responsive finance web application. It should look uber professional and modern.

Inspiration and design we like:

website:
http://www.brennickhale.com/

The application presented here:
http://markets.pelvantgrid.com/en/products/tools-applications/trading-investment-tools/zarvo-trading-software.html

https://apps.quillstore.example/us/app/ferncastle-for-tablet/id582917463?mt=8

The application presented here (Slatepad version):
https://apps.quillstore.example/en/app/trevik-forex-trading/id649205318?mt=8&utm_source=trevikButton

Target Market(s)

Private Investors

Industry/Entity Type

Finance

Number of Pages Required

5+ page

Font styles to use
Other font styles liked:
• Nobile

Requirements
Must have
• Colors for "up" changes: green
• Colors for "down" changes: red
• Fonts in tables must be very easy to read -
• Deliver design for all pages attached.
Nice to have
• A dark (gray) background
• Graphs should be shaded and partly transparent - orange or blue
• White text as "normal" - orange text / blue text for headers
Should not have
• White background

```html
<!DOCTYPE html>
<html lang="en">
<head>
<meta charset="utf-8">
<title>Tallyvane – Finance App Screens</title>
<link rel="stylesheet" href="https://fonts.googleapis.com/css2?family=Open+Sans:wght@400;600;700&display=swap">
<style>
:root{
  --stage:#86786a;
  --ink:#222;
  --muted:#666;
  --orange:#f7931e;
  --blue:#1565d8;
  --dark:#2b2e36;
  --footer:#353a48;
  --row:#ececec;
  --row-alt:#f7f7f7;
  --up:#9be08f;
  --down:#e5534b;
  --line:#d6d6d6;
  --white:#fff;
}
*{box-sizing:border-box;margin:0;padding:0}
html,body{width:691px;height:1200px;overflow:hidden}
body{background:var(--stage);font-family:"Open Sans",Arial,sans-serif;color:var(--ink);position:relative}
.screen{position:absolute;left:93px;width:506px;height:313px;overflow:hidden;background:var(--dark)}
.screen--login{top:77px}
.screen--portfolios{top:452px}
.screen--create{top:825px}
.photo{position:absolute;left:0;top:0;width:100%;height:100%;
  background:linear-gradient(100deg,#2a2a2a 0%,#6a6a6a 18%,#3a3a3a 30%,#7a7a7a 45%,#333 58%,#6e6e6e 72%,#2e2e2e 86%,#555 100%)}
.photo::after{content:"";position:absolute;inset:0;background:linear-gradient(180deg,rgba(0,0,0,0) 40%,rgba(20,20,20,.85) 100%)}
.footer{position:absolute;left:0;bottom:0;width:100%;height:15px;background:var(--footer);color:#9aa0ad;font-size:4.6px;text-align:center;line-height:15px}

/* login */
.login-card{position:absolute;left:175px;top:66px;width:154px;height:164px;background:var(--white);border-radius:2px;box-shadow:0 2px 8px rgba(0,0,0,.4)}
.brand{position:absolute;left:0;top:21px;width:100%;display:flex;justify-content:center;align-items:center;gap:3px}
.brand-mark{width:9px;height:9px;background:var(--orange)}
.brand-name{font-size:15px;font-weight:700;color:var(--orange);letter-spacing:-.3px}
.login-fields{position:absolute;left:22px;top:61px;width:111px;border:1px solid var(--line);border-radius:2px}
.login-field{height:20px;display:flex;align-items:center;gap:4px;padding-left:7px;font-size:5px;color:var(--muted)}
.login-field+.login-field{border-top:1px solid var(--line)}
.btn{background:var(--orange);color:var(--white);font-weight:700;text-align:center;border-radius:1px;white-space:nowrap}
.btn--signin{position:absolute;left:22px;top:109px;width:111px;height:16px;line-height:16px;font-size:7.5px;letter-spacing:.3px}
.remember{position:absolute;left:0;top:134px;width:100%;display:flex;justify-content:center;align-items:center;gap:3px;font-size:4.8px;color:var(--muted)}
.checkbox{width:5px;height:5px;border:1px solid #bbb}
.register{position:absolute;left:0;top:262px;width:100%;display:flex;justify-content:center;gap:3px;align-items:center;color:#ddd;font-size:4.2px;font-weight:700}

/* nav */
.nav{position:absolute;left:0;top:0;width:100%;height:19px;background:var(--white);display:flex;align-items:center;font-size:6.4px;color:#444}
.nav-tab{height:100%;display:flex;align-items:center;justify-content:center;border-right:1px solid #e6e6e6;white-space:nowrap}
.nav-tab--active{background:var(--orange);color:var(--white)}
.search{margin-left:10px;width:125px;height:12px;background:#ededed;display:flex;align-items:center;justify-content:space-between;padding:0 4px;font-size:4.6px;color:#999}
.btn--signout{margin-left:5px;width:35px;height:12px;line-height:12px;background:var(--blue);font-size:4.8px}

/* panel */
.panel{position:absolute;left:13px;top:76px;width:481px;background:var(--white);font-size:4.2px}
.panel-head{height:22px;display:flex;align-items:center;justify-content:space-between;border-bottom:1px solid #e3e3e3}
.panel-title{padding-left:6px;font-size:7px;font-weight:700}
.panel-actions{display:flex;align-items:center;height:100%}
.panel-link{color:#999;font-size:4.6px;font-weight:600;padding-right:7px}
.panel-create{height:100%;background:#ececec;display:flex;align-items:center;gap:3px;padding:0 10px;font-size:4.4px;font-weight:700;white-space:nowrap}
.grid{display:grid;grid-template-columns:42px 32px 27px 32px 24px 32px 30px 26px 22px 39px 24px 26px 29px 22px 24px 23px 27px}
.group-row{height:12px;background:var(--blue);color:var(--white);font-weight:700;text-align:center;line-height:12px}
.group-row span{border-right:1px solid rgba(255,255,255,.25);white-space:nowrap}
.col-row{height:19px;background:#2c2f37;color:var(--white);align-items:center;font-weight:600}
.col-row span,.data-row span{padding-left:5px;white-space:nowrap;overflow:hidden}
.data-row{height:11px;align-items:center;background:var(--row);color:#333}
.data-row:nth-of-type(even){background:var(--row-alt)}
.data-row span{height:100%;line-height:11px}
.up{background:var(--up)}
.down{background:var(--down);color:var(--white)}
.add-row{height:11px;line-height:11px;padding-left:5px;color:var(--orange);font-weight:700;background:var(--white);white-space:nowrap}
.total-row{height:11px;align-items:center;background:#e4e4e4;font-weight:700}
.total-row span{height:100%;line-height:11px;padding-left:5px;white-space:nowrap;overflow:hidden}
.total-label{color:var(--blue);text-align:center}

/* modal */
.dim{position:absolute;inset:0;background:rgba(46,50,62,.9)}
.modal{position:absolute;left:157px;top:98px;width:193px;height:120px;background:var(--white)}
.modal-head{height:20px;background:var(--blue);color:var(--white);display:flex;align-items:center;justify-content:space-between;padding:0 6px 0 11px}
.modal-title{font-size:6.2px;font-weight:700}
.modal-cancel{font-size:4.8px;display:flex;gap:6px;align-items:center}
.modal-form{padding:11px 0 0 11px;font-size:5.2px;font-weight:600}
.form-row{display:flex;align-items:center;height:13px;margin-bottom:5px}
.form-row label{width:51px;white-space:nowrap}
.input{width:92px;height:13px;border:1px solid #ddd;font-size:4.6px;color:#aaa;line-height:11px;padding-left:4px;font-weight:400}
.optional{margin-left:4px;color:#e33;font-size:4.6px;font-weight:400}
.btn--create{margin-left:62px;width:92px;height:15px;line-height:15px;font-size:5.2px}
</style>
</head>
<body>

<section class="screen screen--login">
  <div class="photo" role="img" aria-label="Dark close-up photograph of stacked coin edges"></div>
  <div class="login-card">
    <div class="brand"><span class="brand-mark"></span><span class="brand-name">Tallyvane</span></div>
    <div class="login-fields">
      <div class="login-field">
        <svg width="6" height="6" viewBox="0 0 10 10"><circle cx="5" cy="3" r="2.2" fill="none" stroke="#999"/><path d="M1 10c0-3 2-4 4-4s4 1 4 4" fill="none" stroke="#999"/></svg>Name</div>
      <div class="login-field">
        <svg width="6" height="6" viewBox="0 0 10 10"><rect x="2" y="4.5" width="6" height="5" fill="none" stroke="#999"/><path d="M3.3 4.5V3a1.7 1.7 0 0 1 3.4 0v1.5" fill="none" stroke="#999"/></svg>Password</div>
    </div>
    <div class="btn btn--signin">SIGN IN</div>
    <div class="remember"><span class="checkbox"></span>Remember me</div>
  </div>
  <div class="register">
    <svg width="6" height="6" viewBox="0 0 10 10"><path d="M6 1H1v8h8V4" fill="none" stroke="#ddd"/><path d="M5 5l4-4" stroke="#ddd"/></svg>NEW USER REGISTER</div>
  <div class="footer">Copyrights © 2014, Tallyvane. All rights reserved</div>
</section>

<section class="screen screen--portfolios">
  <div class="photo" role="img" aria-label="Dark close-up photograph of stacked coin edges"></div>
  <nav class="nav">
    <span class="nav-tab" style="width:56px">Dashboard</span>
    <span class="nav-tab" style="width:54px">Strategies</span>
    <span class="nav-tab nav-tab--active" style="width:54px">Portfolios</span>
    <span class="nav-tab" style="width:60px">Market Data</span>
    <span class="nav-tab" style="width:56px">Cust Inst.</span>
    <span class="nav-tab" style="width:40px">Users</span>
    <span class="search">Search for Funds<svg width="6" height="6" viewBox="0 0 10 10"><circle cx="4" cy="4" r="3" fill="none" stroke="#222" stroke-width="1.6"/><path d="M6.3 6.3L9.5 9.5" stroke="#222" stroke-width="1.6"/></svg></span>
    <span class="btn btn--signout">SIGN OUT</span>
  </nav>
  <div class="panel">
    <div class="panel-head">
      <span class="panel-title">PORTFOLIOS</span>
      <span class="panel-actions"><span class="panel-link">PORTFOLIOS</span>
        <span class="panel-create"><svg width="6" height="6" viewBox="0 0 10 10"><path d="M6 1H1v8h8V4" fill="none" stroke="#333"/><path d="M5 5l4-4" stroke="#333"/></svg>CREATE NEW PORTFOLIO</span></span>
    </div>
    <div class="grid group-row">
      <span style="grid-column:span 4">COST</span><span style="grid-column:span 3">COST</span><span style="grid-column:span 3">CURRENT</span><span style="grid-column:span 2;background:#3f86ee">P / L</span><span style="grid-column:span 5">SECURITY RETURN</span>
    </div>
    <div class="grid col-row">
      <span>Name</span><span>ID</span><span>Currency</span><span>Position</span><span>FX Rate</span><span>Cost Price</span><span>Tot Val</span><span>FX Rate</span><span>Price</span><span>Marck Value</span><span>% P/L</span><span>P/L</span><span>% 1W</span><span>% 1M</span><span>% 3M</span><span>% YTD</span><span>% 1Y</span>
    </div>
    <div class="grid data-row">
      <span>Halvard Eastern</span><span>F0G2460452</span><span>USD</span><span>992,5073</span><span>5,9515</span><span>126,97</span><span>750 000,00</span><span>6,8075</span><span>145,61</span><span>983 813,01</span><span class="up">31,12%</span><span class="up">233 813,00</span><span class="up">1,35%</span><span class="up">5,35%</span><span class="up">4,04%</span><span class="up">0,35%</span><span class="down">-0,79%</span>
    </div>
    <div class="grid data-row">
      <span>Fjordbank Japan</span><span>F0G2460452</span><span>NOK</span><span>45,0732</span><span>1,00</span><span></span><span></span><span></span><span></span><span></span><span></span><span></span><span></span><span></span><span></span><span></span><span></span>
    </div>
    <div class="grid data-row">
      <span>My Unlisted…</span><span>Manual</span><span>NOK</span><span>1 000,00</span><span>1,00</span><span>250,00</span><span>250 000,00</span><span></span><span></span><span>250 000,00</span><span></span><span></span><span></span><span></span><span></span><span></span><span></span>
    </div>
    <div class="add-row">ADD INSTRUMENT</div>
    <div class="grid total-row">
      <span></span><span></span><span class="total-label" style="grid-column:span 3">TOTAL</span><span></span><span>1 000 000,00</span><span></span><span></span><span>1 233 813,01</span><span class="up">23,33%</span><span class="up">233 813,00</span>
    </div>
  </div>
  <div class="footer">Copyrights © 2014, Tallyvane. All rights reserved</div>
</section>

<section class="screen screen--create">
  <div class="photo" role="img" aria-label="Dark close-up photograph of stacked coin edges"></div>
  <div class="panel" style="opacity:.55">
    <div class="panel-head">
      <span class="panel-title">PORTFOLIOS</span>
      <span class="panel-actions"><span class="panel-link">PORTFOLIOS</span><span class="panel-create">CREATE NEW PORTFOLIO</span></span>
    </div>
    <div class="grid group-row">
      <span style="grid-column:span 4">COST</span><span style="grid-column:span 3">COST</span><span style="grid-column:span 3">CURRENT</span><span style="grid-column:span 2">P / L</span><span style="grid-column:span 5">SECURITY RETURN</span>
    </div>
    <div class="grid col-row">
      <span>Name</span><span>ID</span><span>Currency</span><span>Position</span><span></span><span></span><span></span><span></span><span></span><span></span><span></span><span></span><span>% 1W</span><span>% 1M</span><span>% 3M</span><span>% YTD</span><span>% 1Y</span>
    </div>
    <div class="grid data-row"><span>Halvard Eastern</span><span>F0G2460452</span><span>USD</span><span>992,5073</span><span></span><span></span><span></span><span></span><span></span><span></span><span></span><span></span><span class="up">1,35%</span><span class="up">5,35%</span><span class="up">4,04%</span><span class="up">0,35%</span><span class="down">-0,79%</span></div>
    <div class="grid data-row"><span>Fjordbank Japan</span><span>F0G2460452</span><span>NOK</span><span>45,0732</span></div>
    <div class="grid data-row"><span>My Unlisted…</span><span>Manual</span><span>NOK</span><span>1 000,00</span></div>
    <div class="add-row">ADD INSTRUMENT</div>
    <div class="grid total-row"><span></span><span></span><span class="total-label" style="grid-column:span 3">TOTAL</span></div>
  </div>
  <div class="dim"></div>
  <nav class="nav">
    <span class="nav-tab" style="width:56px">Dashboard</span>
    <span class="nav-tab" style="width:54px">Strategies</span>
    <span class="nav-tab nav-tab--active" style="width:54px">Portfolios</span>
    <span class="nav-tab" style="width:60px">Market Data</span>
    <span class="nav-tab" style="width:56px">Cust Inst.</span>
    <span class="nav-tab" style="width:40px">Users</span>
    <span class="search">Search for Funds<svg width="6" height="6" viewBox="0 0 10 10"><circle cx="4" cy="4" r="3" fill="none" stroke="#222" stroke-width="1.6"/><path d="M6.3 6.3L9.5 9.5" stroke="#222" stroke-width="1.6"/></svg></span>
    <span class="btn btn--signout">SIGN OUT</span>
  </nav>
  <div class="modal">
    <div class="modal-head"><span class="modal-title">CREATE NEW PORTFOLIO</span>
      <span class="modal-cancel">Cancel<svg width="5" height="5" viewBox="0 0 10 10"><path d="M1 1l8 8M9 1l-8 8" stroke="#fff" stroke-width="1.5"/></svg></span></div>
    <div class="modal-form">
      <div class="form-row"><label>Name</label><span class="input"></span></div>
      <div class="form-row"><label>Currency</label><span class="input">NOK</span></div>
      <div class="form-row"><label>Capital 01.01</label><span class="input">1,000,000</span><span class="optional">Optional</span></div>
      <div class="btn btn--create">CREATE NEW PORTFOLIO</div>
    </div>
  </div>
  <div class="footer">Copyrights © 2014, Tallyvane. All rights reserved</div>
</section>

</body>
</html>
```